RivoCounsel Compensation Lawyers

We need a modern, sleek letterhead that is professional.

In relation to the footer, we would like to have firm contact details there ideally, however you must also insert at the bottom of each page the following....

Liability limited by a scheme approved under the Professional Standards Legislation.

From the attachment you can extract the firm logo. Also, I would like the Accredited specialist circle on the letterhead also.

Also, I would like you to create a document that can easily be edited for change of contact details, as these are likely to change.

Industry/Entity Type

It Professional

Font styles to use
Sans Serif

Colors
0655a3
3276b5
85abd2
0492cd
33a6d7
85cae6
cee9f5
eaf1f7
cbcbcb

Requirements
Must have
• Ph: 8371-5264
• F: 8815-3927
• M 0468-253-914
• mk@rivocounsel.example.au
• www.rivocounsel.example.au
Nice to have
• the word document gives you an idea of what I like. I am happy for your to amaze me with your creativity.

```html
<!DOCTYPE html>
<html lang="en">
<head>
<meta charset="utf-8">
<title>RivoCounsel Compensation Lawyers — Letterhead</title>
<link href="https://fonts.googleapis.com/css2?family=Arimo:wght@400&family=Source+Sans+3:wght@400&display=swap" rel="stylesheet">
<style>
  :root {
    --brand-deep: #0655a3;
    --brand-mid: #3276b5;
    --brand-sky: #33a6d7;
    --bar-light: #4fb8e6;
    --bar-dark: #2a83cb;
    --ink: #111111;
    --ink-soft: #555555;
    --seal: #cbcbcb;
    --paper: #ffffff;
  }
  html, body {
    margin: 0;
    padding: 0;
    width: 1011px;
    height: 1200px;
    overflow: hidden;
    background: var(--paper);
  }
  .letterhead {
    position: relative;
    width: 1011px;
    height: 1200px;
    background: var(--paper);
    font-family: "Arimo", Arial, sans-serif;
  }
  .top-band {
    position: absolute;
    top: 0; left: 0;
    width: 100%;
    height: 15px;
    display: flex;
  }
  .top-band__light { flex: 0 0 651px; background: var(--bar-light); }
  .top-band__dark { flex: 1; background: var(--bar-dark); }

  .firm-name {
    position: absolute;
    left: 107px;
    top: 150px;
    margin: 0;
    font-family: "Source Sans 3", "Myriad Pro", sans-serif;
    font-weight: 400;
    font-size: 33px;
    line-height: 40px;
    color: var(--brand-deep);
  }
  .firm-name span { display: block; }

  .office {
    position: absolute;
    left: 685px;
    top: 48px;
    font-size: 18px;
    line-height: 23px;
    letter-spacing: 0.6px;
    color: var(--ink-soft);
    font-style: normal;
    white-space: nowrap;
  }
  .office__title { color: var(--ink); }
  .office__line { display: block; }

  .footer {
    position: absolute;
    left: 0;
    right: 0;
    top: 1090px;
  }
  .footer__practice,
  .footer__liability {
    position: absolute;
    right: 166px;
    margin: 0;
    white-space: nowrap;
    text-align: right;
    color: var(--ink);
  }
  .footer__practice {
    top: 8px;
    font-size: 19px;
    letter-spacing: 0.8px;
  }
  .footer__liability {
    top: 40px;
    font-size: 14px;
    letter-spacing: 0.5px;
  }
  .footer__seal {
    position: absolute;
    left: 866px;
    top: 4px;
  }
</style>
</head>
<body>
  <main class="letterhead">
    <div class="top-band">
      <div class="top-band__light"></div>
      <div class="top-band__dark"></div>
    </div>

    <h1 class="firm-name">
      <span>RivoCounsel</span>
      <span>Compensation Lawyers</span>
    </h1>

    <address class="office">
      <span class="office__line office__title">Harbourside Office</span>
      <span class="office__line">P.O. Box B417 Westbrook</span>
      <span class="office__line">South NSW 2190</span>
      <span class="office__line">Ph: 8371-5264</span>
      <span class="office__line">F:&nbsp;&nbsp;&nbsp;8815-3927</span>
      <span class="office__line">M: 0468-253-914</span>
      <span class="office__line">mk@rivocounsel.example.au</span>
      <span class="office__line">www.rivocounsel.example.au</span>
    </address>

    <footer class="footer">
      <p class="footer__practice">INSURANE LAW | ESTATE &amp; PROPERTY LAW | FAMILY LAW | COMMERCIAL LAW</p>
      <p class="footer__liability">Liability limited by a scheme approved under the Professional Standards Legislation.</p>
      <svg class="footer__seal" width="62" height="62" viewBox="0 0 62 62" role="img" aria-label="Accredited specialist seal">
        <circle cx="31" cy="31" r="29" fill="none" stroke="var(--seal)" stroke-width="2"/>
        <circle cx="31" cy="31" r="20" fill="var(--brand-mid)"/>
      </svg>
    </footer>
  </main>
</body>
</html>
```